Landscaping business card

We need a business card that reflects our business. We do lawncare and landscaping with all natural materials and have a great track record in the communities we serve: Newton, Brookline, Wellesley, Brighton, Watertown, and Waltham. We have been in business for 10 years.
Updates

I don't know the curvy fonts. Please keep the fonts fairly conservative.

Industry/Entity Type

Landscaping

Contact Information for Business Card

Verbeck Landscaping
Dale Verbeck
Founder and CEO
847 Tarrow Ave
Ashmere, CT 02317

Requirements
Must have
• The color green

```html
<!DOCTYPE html>
<html lang="en">
<head>
<meta charset="utf-8">
<title>Verbeck Landscaping – Business Card</title>
<link rel="stylesheet" href="https://fonts.googleapis.com/css2?family=Kreon:wght@300&family=Open+Sans:wght@400&display=swap">
<style>
  :root {
    --brand-green: #1b8a35;
    --rule-green: #2a8f3c;
    --ink-grey: #555557;
    --paper: #ffffff;
    --stone-light: #b9b9b5;
    --stone-mid: #9c9c98;
    --grass-light: #4aa834;
    --grass-deep: #2b8420;
  }
  html, body {
    margin: 0;
    padding: 0;
    overflow: hidden;
    background: var(--paper);
  }
  .card {
    position: relative;
    width: 1200px;
    height: 715px;
    background: var(--paper);
    overflow: hidden;
  }
  .hero-band {
    position: absolute;
    left: 0;
    top: 189px;
    width: 1200px;
    height: 182px;
    background:
      linear-gradient(180deg, rgba(255,255,255,0.08) 0%, rgba(0,0,0,0.12) 100%),
      linear-gradient(100deg, var(--stone-light) 0%, var(--stone-mid) 22%, #8d9a7c 36%, var(--grass-light) 46%, #3b9a2a 70%, var(--grass-deep) 100%);
  }
  .company-name {
    position: absolute;
    left: 84px;
    top: 86px;
    margin: 0;
    font-family: "Open Sans", Arial, sans-serif;
    font-weight: 400;
    font-size: 68px;
    line-height: 1;
    color: var(--brand-green);
    white-space: nowrap;
  }
  .person-name {
    position: absolute;
    left: 150px;
    top: 412px;
    margin: 0;
    font-family: "Kreon", Georgia, serif;
    font-weight: 300;
    font-size: 58px;
    line-height: 1;
    font-variant: small-caps;
    letter-spacing: 2px;
    color: var(--ink-grey);
    white-space: nowrap;
  }
  .person-title {
    position: absolute;
    left: 520px;
    top: 466px;
    margin: 0;
    font-family: "Open Sans", Arial, sans-serif;
    font-size: 23px;
    line-height: 1;
    color: var(--ink-grey);
    white-space: nowrap;
  }
  .address {
    position: absolute;
    top: 547px;
    margin: 0;
    font-family: "Open Sans", Arial, sans-serif;
    font-size: 33px;
    line-height: 1;
    color: var(--ink-grey);
    white-space: nowrap;
    font-style: normal;
  }
  .address-street {
    right: 700px;
  }
  .address-city {
    left: 537px;
  }
  .address-divider {
    position: absolute;
    left: 517px;
    top: 531px;
    width: 2px;
    height: 82px;
    background: var(--rule-green);
  }
</style>
</head>
<body>
  <main class="card">
    <h1 class="company-name">Verbeck Landscaping</h1>

    <div class="hero-band" role="img" aria-label="Photo of curved granite stone steps beside a green lawn"></div>

    <p class="person-name">Dale Verbeck</p>
    <p class="person-title">FOUNDER and CEO</p>

    <address class="address address-street">847 Tarrow Ave</address>
    <div class="address-divider"></div>
    <address class="address address-city">Ashmere, CT 02317</address>
  </main>
</body>
</html>
```